Brellwick Finance Stationary Design

We have selected a logo as our winner, we now need a full stationary set to be in the same theme.
Required:
- Letter Head
- Business Card Template
- Custom Envelopes
- A5 Notepad Design (Front cover and content pages. Content pages blank(no lines) but with our branding on them,)
- With Compliments Slip
Updates

Hey All,

We have changed the colour scheme of our logo. Our apologies if anyone has begun designing based off the old scheme. Please see the updated scheme in the brief,

Tobin

Target Market(s)

Target market is experienced property developers and financial institutions.

Industry/Entity Type

Commercial Finance

Font styles to use
Serif

Colors
0054AA
0677BA
7BADD7
CADEEF
E8F1F8
0094D4
00A9DD
6FCCEA
C7EBF8
E9F6FB
00AB8E
00BBA5
67D7C9
C6EFE9
E9F9F6
59FF00
82FF00
B8FF75
E3FFCB
F4FFEA

```html
<!DOCTYPE html>
<html lang="en">
<head>
<meta charset="utf-8">
<title>Brellwick Finance Stationery Set</title>
<link rel="stylesheet" href="https://fonts.googleapis.com/css2?family=Montserrat:wght@400;600;700&family=Raleway:wght@400;500&family=Tinos:wght@700&display=swap">
<style>
  :root {
    --blue: #22409a;
    --green: #1e8a3c;
    --bg: #dcdde0;
    --paper: #ffffff;
    --grey: #8a8a8a;
    --text: #6f6f6f;
  }
  * { box-sizing: border-box; margin: 0; padding: 0; }
  html, body { width: 995px; height: 1200px; overflow: hidden; }
  body { background: var(--bg); font-family: "Raleway", sans-serif; color: var(--text); position: relative; }
  .sheet { position: absolute; background: var(--paper); overflow: hidden; }
  .wordmark { position: absolute; font-family: "Montserrat", sans-serif; font-weight: 700; color: var(--blue); letter-spacing: .02em; white-space: nowrap; text-transform: uppercase; }
  .rule { position: absolute; left: 0; right: 0; height: 1.5px; background: var(--green); }
  .band { position: absolute; left: 0; right: 0; bottom: 0; background: var(--blue); color: #fff; display: flex; align-items: center; justify-content: center; font-family: "Montserrat", sans-serif; }
  .contact { position: absolute; font-family: "Montserrat", sans-serif; color: var(--grey); line-height: 1; }
  .contact li { list-style: none; display: flex; align-items: center; gap: 2px; }
  .contact svg { flex: none; }

  /* business card front */
  .card-front { left: 37px; top: 51px; width: 225px; height: 135px; }
  .card-front .wordmark { left: 0; right: 0; top: 26px; text-align: center; font-size: 11px; }
  .card-front .person { position: absolute; right: 131px; top: 76px; text-align: right; font-family: "Montserrat", sans-serif; }
  .card-front .person-name { color: var(--blue); font-size: 8.5px; font-weight: 600; }
  .card-front .person-role { color: var(--grey); font-size: 4.5px; margin-top: 1px; }
  .card-front .divider { position: absolute; left: 137px; top: 68px; width: .6px; height: 30px; background: #bbb; }
  .card-front .contact { left: 141px; top: 70px; font-size: 5.5px; }
  .card-front .contact li { margin-bottom: 3.8px; }
  .card-front .rule { top: 107px; }
  .card-front .band { height: 24px; font-size: 5px; }

  /* business card back */
  .card-back { left: 278px; top: 51px; width: 225px; height: 135px; background: var(--blue); }
  .card-back .wordmark { left: 0; right: 0; top: 60px; text-align: center; font-size: 11px; color: #fff; }

  /* envelope */
  .envelope { left: 37px; top: 209px; width: 466px; height: 234px; }
  .envelope .wordmark { left: 17px; top: 24px; font-size: 11px; }
  .envelope .rule { top: 208px; }
  .envelope .band { height: 24px; font-size: 7px; }

  /* compliment slip */
  .slip { left: 38px; top: 459px; width: 465px; height: 213px; }
  .slip .wordmark { left: 14px; top: 26px; font-size: 11px; }
  .slip .slip-title { position: absolute; right: 16px; top: 17px; font-family: "Tinos", serif; font-weight: 700; font-size: 15.5px; color: var(--blue); letter-spacing: .01em; }
  .slip .contact { left: 12px; top: 154px; font-size: 6.8px; }
  .slip .contact li { margin-bottom: 3.2px; }
  .slip .rule { top: 189px; }
  .slip .band { height: 20px; }

  /* letterhead */
  .letterhead { left: 519px; top: 51px; width: 440px; height: 621px; }
  .letterhead .wordmark { left: 23px; top: 36px; font-size: 12.5px; }
  .letterhead .contact { right: 22px; top: 32px; font-size: 7px; text-align: right; }
  .letterhead .contact li { justify-content: flex-end; margin-bottom: 3.5px; }
  .recipient { position: absolute; left: 26px; top: 164px; font-family: "Montserrat", sans-serif; color: var(--grey); font-size: 8px; }
  .recipient-name { font-weight: 700; color: var(--blue); font-size: 14px; margin-bottom: 4px; }
  .recipient p { margin-bottom: 5px; line-height: 1.2; }
  .letter-date { position: absolute; right: 23px; top: 220px; font-family: "Montserrat", sans-serif; font-weight: 600; font-size: 8.5px; color: var(--grey); }
  .letter-body { position: absolute; left: 24px; top: 251px; width: 393px; font-size: 7.6px; line-height: 9.9px; text-align: justify; }
  .letter-body p { margin-bottom: 10px; }
  .letter-body p.tight { margin-bottom: 0; }
  .letter-body p.gap { margin-top: 20px; }
  .signoff { position: absolute; right: 30px; top: 475px; font-size: 11px; color: var(--grey); }
  .signature { position: absolute; left: 320px; top: 498px; width: 82px; height: 52px; background: linear-gradient(90deg, #f2f2f2, #e6e6e6); }
  .letterhead .rule { top: 589px; }
  .letterhead .band { height: 29px; font-size: 7px; }

  /* notepad cover */
  .notepad-cover { left: 141px; top: 732px; width: 319px; height: 425px; background: linear-gradient(180deg, #f4f5f6, #ffffff); }
  .notepad-cover .wordmark { left: 0; right: 0; top: 197px; text-align: center; font-size: 22px; }
  .notepad-cover .rule { top: 332px; height: 2.5px; }
  .notepad-cover .band { height: 87px; flex-direction: column; justify-content: flex-start; padding-top: 10px; }
  .notepad-title { font-family: "Montserrat", sans-serif; font-weight: 600; font-size: 31px; line-height: 1; }
  .notepad-blurb { margin-top: 9px; width: 245px; text-align: center; font-size: 4.4px; line-height: 5.4px; }
  .notepad-blurb p + p { margin-top: 6px; }

  /* notepad inner page */
  .notepad-page { left: 545px; top: 732px; width: 319px; height: 425px; }
  .notepad-page .rule { top: 401px; }
  .notepad-page .band { height: 20px; justify-content: flex-end; padding-right: 8px; font-size: 4.8px; }
</style>
</head>
<body>

<svg width="0" height="0" style="position:absolute">
  <defs>
    <symbol id="icon-phone" viewBox="0 0 10 10"><circle cx="5" cy="5" r="5" fill="#1e8a3c"/><path d="M3.3 2.6c.4-.3.7-.2.9.2l.4.8c.1.3 0 .5-.2.7l-.3.2c.3.7.8 1.2 1.4 1.5l.3-.3c.2-.2.4-.2.7-.1l.8.4c.4.2.4.6.1.9-.8.8-2 .5-3.2-.6S2.5 3.4 3.3 2.6z" fill="#fff"/></symbol>
    <symbol id="icon-mail" viewBox="0 0 10 10"><circle cx="5" cy="5" r="5" fill="#1e8a3c"/><rect x="2.6" y="3.3" width="4.8" height="3.4" rx=".4" fill="#fff"/><path d="M2.8 3.6 5 5.3l2.2-1.7" stroke="#1e8a3c" stroke-width=".6" fill="none"/></symbol>
    <symbol id="icon-web" viewBox="0 0 10 10"><circle cx="5" cy="5" r="5" fill="#1e8a3c"/><circle cx="5" cy="5" r="2.6" stroke="#fff" stroke-width=".6" fill="none"/><path d="M2.4 5h5.2M5 2.4c-1.2 1.5-1.2 3.7 0 5.2M5 2.4c1.2 1.5 1.2 3.7 0 5.2" stroke="#fff" stroke-width=".5" fill="none"/></symbol>
  </defs>
</svg>

<section class="sheet card-front">
  <div class="wordmark">Brellwick Finance</div>
  <div class="person">
    <div class="person-name">MARA QUILL</div>
    <div class="person-role">Director / CEO</div>
  </div>
  <div class="divider"></div>
  <ul class="contact">
    <li><svg width="5" height="5"><use href="#icon-phone"/></svg>111-222-333</li>
    <li><svg width="5" height="5"><use href="#icon-mail"/></svg>info@brellwickfinance.com</li>
    <li><svg width="5" height="5"><use href="#icon-web"/></svg>www.brellwickfinance.com</li>
  </ul>
  <div class="rule"></div>
  <div class="band">1234 City Your Ln. Suite, 123 Dallas, TX 0000</div>
</section>

<section class="sheet card-back">
  <div class="wordmark">Brellwick Finance</div>
</section>

<section class="sheet envelope">
  <div class="wordmark">Brellwick Finance</div>
  <div class="rule"></div>
  <div class="band">1234 City Your Ln. Suite, 123 Dallas, TX 0000</div>
</section>

<section class="sheet slip">
  <div class="wordmark">Brellwick Finance</div>
  <h2 class="slip-title">WITH COMPLIMENT</h2>
  <ul class="contact">
    <li><svg width="6" height="6"><use href="#icon-phone"/></svg>111-222-333</li>
    <li><svg width="6" height="6"><use href="#icon-mail"/></svg>info@brellwickfinance.com</li>
    <li><svg width="6" height="6"><use href="#icon-web"/></svg>www.brellwickfinance.com</li>
  </ul>
  <div class="rule"></div>
  <div class="band"></div>
</section>

<section class="sheet letterhead">
  <div class="wordmark">Brellwick Finance</div>
  <ul class="contact">
    <li>111-222-333 <svg width="6" height="6"><use href="#icon-phone"/></svg></li>
    <li>info@brellwickfinance.com <svg width="6" height="6"><use href="#icon-mail"/></svg></li>
    <li>www.brellwickfinance.com <svg width="6" height="6"><use href="#icon-web"/></svg></li>
  </ul>
  <div class="recipient">
    <div class="recipient-name">MARA QUILL</div>
    <p>0123-456-789</p>
    <p>info@brellwickfinance.com</p>
    <p>1234 City Your Ln. Suite<br>123 Dallas, TX 0000</p>
  </div>
  <div class="letter-date">12 December, 2023</div>
  <div class="letter-body">
    <p>Lorem ipsum dolor sit amet, consectetuer adipiscing elit, sed diam nonummy nibh euismod tincidunt ut laoreet dolore magna aliquam erat volutpat. Ut wisi enim ad minim veniam, quis nostrud exerci tation ullamcorper suscipit lobortis nisl ut aliquip ex ea commodo consequat. Duis autem vel eum iriure dolor in hendrerit in vulputate velit esse molestie consequat, vel illum dolore eu feugiat nulla facilisis at vero eros et accumsan et iusto odio dignissim qui blandit praesent luptatum zzril delenit augue duis dolore te feugait nulla facilisi.</p>
    <p class="tight">Lorem ipsum dolor sit amet, cons ectetuer adipiscing elit, sed diam nonummy nibh euismod tincidunt ut laoreet dolore magna aliquam erat volutpat. Ut wisi enim ad minim veniam, quis nostrud exerci tation ullamcorper suscipit lobortis nisl ut aliquip ex ea commodo consequat.</p>
    <p>Lorem ipsum dolor sit amet, consectetuer adipiscing elit, sed diam nonummy nibh euismod tincidunt ut laoreet dolore magna aliquam erat</p>
    <p class="gap">Lorem ipsum dolor sit amet, cons ectetuer adipiscing elit, sed diam nonummy nibh euismod tincidunt ut laoreet dolore magna aliquam erat volutpat. Ut wisi enim ad minim veniam, quis nostrud exerci tation ullamcorper suscipit lobortis nisl ut aliquip ex ea commodo consequat. Lorem ipsum dolor sit zamet, consectetuer adipiscing elit, sed diam nonummy nibh euismod tincidunt.</p>
  </div>
  <div class="signoff">Managing Director</div>
  <div class="signature" role="img" aria-label="Handwritten signature of the managing director"></div>
  <div class="rule"></div>
  <div class="band">1234 City Your Ln. Suite, 123 Dallas, TX 0000</div>
</section>

<section class="sheet notepad-cover">
  <div class="wordmark">Brellwick Finance</div>
  <div class="rule"></div>
  <div class="band">
    <div class="notepad-title">Notepad</div>
    <div class="notepad-blurb">
      <p>Lorem ipsum dolor sit amet, consectetuer adipiscing elit, sed diam nonummy nibh euismod tincidunt ut laoreet dolore magna aliquam erat volutpat. Ut wisi enim ad minim veniam</p>
      <p>quis nostrud exerci tation ullamcorper suscipit lobortis nisl ut aliquip ex ea commodo consequat. Duis autem vel eum iriure dolor in hendrerit in vulputate velit esse molestie consequat, vel illum dolore eu</p>
    </div>
  </div>
</section>

<section class="sheet notepad-page">
  <div class="rule"></div>
  <div class="band">Page 2</div>
</section>

</body>
</html>
```